Web Design Project

Full website, similar _function_ to http://www.kindmarrow.com/
You can not only make charities, but also communicate social or environmental problems by posting them on the website.
I need a full layout design, right now I am using a slightly changed bootstrap. View attached file "basic css" for current containers layout
Including front page, static text page (SEO), show listing page and content page, all the same look and feel. Dont focus to hard on the charity part...

Logo will be needed:
The URL - also the Logo - is Wehklang.de - that is German for "Outcry" - so working with a "!" makes prob. sense, like Wehklang!de or so... (EXTRA)

Colour Scheme:
I do not have a colour scheme, but I alreay think "Red URL with green elements" would be nice - that means please give me some other ideas ... I am not a designer, right?! :)

NO CODING NEEDED
Updates

Project Deadline Extended
Reason: I just got too few designs, some nice with it, though - I will clarify my needs new so it will be easier to reply with suggestions! :)

Target Market(s)

People who want to do charity and help other people

Industry/Entity Type

Charity

Requirements
Must have
• responsive design (tablet, smartphone)
static frame header (like here at pixelforum)

```html
<!DOCTYPE html>
<html lang="en">
<head>
<meta charset="utf-8">
<title>Charity Platform — Home</title>
<link rel="stylesheet" href="https://fonts.googleapis.com/css2?family=PT+Sans:ital,wght@0,400;0,700;1,400&family=PT+Sans+Narrow:wght@400;700&family=Rokkitt:wght@400&display=swap">
<style>
:root{
  --topbar:#2b0d0e;
  --nav-top:#b63c3c;
  --nav-bottom:#962727;
  --nav-active:#3d1010;
  --topbar-link:#e36a63;
  --page:#fbeeee;
  --panel:#ffffff;
  --green-top:#2f7a35;
  --green-bottom:#1d5a22;
  --green-dark:#174a1b;
  --green-text:#1f6a26;
  --link-green:#5fbf2a;
  --body-text:#2a2a2a;
  --footer:#6c1515;
  --footer-text:#f3dede;
  --footer-muted:#c97a74;
  --footer-line:#8c3030;
  --copyright:#430b0c;
}
*{box-sizing:border-box;margin:0;padding:0}
html,body{width:964px;height:1200px;overflow:hidden}
body{background:var(--page);font-family:"PT Sans",sans-serif;color:var(--body-text);position:relative}
a{color:inherit;text-decoration:none}
.abs{position:absolute}

/* top bar */
.topbar{left:0;top:0;width:964px;height:27px;background:var(--topbar)}
.topbar .home{left:141px;top:6px}
.topbar .account{right:104px;top:6px;font-size:12px;color:var(--topbar-link)}
.topbar .account span{margin:0 7px;color:var(--topbar-link)}

/* main navigation */
.mainnav{left:0;top:27px;width:964px;height:58px;background:linear-gradient(var(--nav-top),var(--nav-bottom));box-shadow:0 2px 3px rgba(0,0,0,.35);z-index:2}
.brand{left:141px;top:5px;font-family:"Rokkitt",serif;font-size:44px;color:#fff;letter-spacing:-1.5px}
.menu{left:307px;top:0;display:flex;height:58px}
.menu a{display:block;padding:0 10px;line-height:58px;font-weight:700;font-size:13px;color:#fff;border-right:1px solid rgba(0,0,0,.18);box-shadow:1px 0 0 rgba(255,255,255,.1)}
.menu a:last-child{border:none;box-shadow:none}
.menu a.active{color:var(--nav-active)}

/* hero */
.hero{left:0;top:85px;width:964px;height:429px;background:
  radial-gradient(ellipse 190px 260px at 860px 300px,#c9867c 0%,#a7625a 55%,transparent 100%),
  linear-gradient(180deg,#a98178 0%,#b89186 30%,#9c7066 65%,#7e5048 100%)}
.hero-caption{left:99px;top:376px;width:279px;height:108px;border-radius:8px;background:rgba(38,62,30,.82);color:#fff;padding:9px 15px}
.hero-caption p{font-size:16px;line-height:31px}
.hero-caption b{font-size:20px}
.hero-caption .more{position:absolute;right:28px;bottom:12px;font-size:15px;font-weight:700;color:var(--link-green);text-decoration:underline}
.slider-dots{left:431px;top:500px;width:86px;height:25px;border-radius:13px;background:linear-gradient(#fff,#e6e6e6);box-shadow:0 1px 3px rgba(0,0,0,.3);display:flex;gap:6px;justify-content:center;align-items:center}
.slider-dots i{width:12px;height:12px;border-radius:50%;border:1px solid #b9b9b9;background:#f4f4f4}
.slider-dots i.on{background:#c9c9c9}

/* teaser */
.teaser{left:81px;top:545px;width:788px;height:160px;background:var(--panel);border-radius:6px;overflow:hidden}
.teaser-head{height:35px;background:linear-gradient(var(--green-top),var(--green-bottom));display:flex}
.teaser-head h3{width:397px;padding-left:19px;font-weight:400;font-size:14px;color:#fff;line-height:35px;display:flex;align-items:center;gap:8px}
.teaser-col{position:absolute;top:47px;width:356px;font-size:11px;line-height:15.6px}
.teaser-col.left{left:17px}
.teaser-col.right{left:414px}
.teaser-divider{left:391px;top:42px;height:112px;border-left:1px dashed #c8c8c8}

/* sidebar */
.sidenav{left:82px;top:724px;width:196px}
.sidenav .item{height:30px;background:linear-gradient(var(--green-top),var(--green-bottom));border-bottom:1px solid var(--green-dark);color:#fff;font-size:13px;display:flex;align-items:center;gap:9px;padding-left:11px}
.sidenav .item.current{height:32px;background:linear-gradient(#23682a,#16501b)}
.sidenav .sub{height:30px;background:#fff;border-bottom:1px solid #e8e0e0;font-size:11.5px;display:flex;align-items:center;padding-left:22px;gap:8px}
.sidenav .sub::before{content:"";border-left:4px solid var(--green-text);border-top:3px solid transparent;border-bottom:3px solid transparent}

/* content */
.section-title{font-family:"PT Sans Narrow",sans-serif;font-weight:700;font-size:15px;color:var(--green-text);text-decoration:underline}
.thumb{border:1px solid #8a9d8a}
.blog-text{font-size:11px;line-height:15.6px}
.blog-text.small{font-family:"PT Sans Narrow",sans-serif;font-size:9.5px;line-height:15.6px}
.post-text{font-size:11px;line-height:15.4px;width:210px}
.post-text .date{display:block;font-style:italic;color:var(--green-text);text-decoration:underline}

/* footer */
.footer{left:0;top:1028px;width:964px;height:144px;background:var(--footer);border-top:2px solid #4b0c0c}
.fcol{position:absolute;top:18px}
.fcol h4{font-weight:400;font-size:13.5px;color:var(--footer-text);margin-bottom:9px}
.fcol a{display:block;font-size:11px;color:var(--footer-muted);border-top:1px solid var(--footer-line);padding-top:4px;height:25px}
.subscribe{left:646px;top:20px;color:var(--footer-text);font-size:12.5px}
.email{position:absolute;top:22px;left:0;width:196px;height:30px;background:#fff;border-radius:3px;overflow:hidden;font-size:12px;color:#333;line-height:30px;padding-left:7px}
.email .go{position:absolute;right:0;top:0;width:41px;height:30px;background:linear-gradient(#4ea23e,#2d7a25);display:flex;align-items:center;justify-content:center}
.follow{position:absolute;top:63px;left:0;font-size:12.5px}
.socials{position:absolute;top:86px;left:0;display:flex;gap:10px}
.socials span{width:26px;height:26px;border-radius:50%;background:linear-gradient(#4a4a4a,#2c2c2c);box-shadow:0 1px 2px rgba(0,0,0,.4)}
.copyright{left:0;top:1172px;width:964px;height:28px;background:var(--copyright);color:var(--footer-text);font-size:9.5px;line-height:28px;padding-left:81px}
</style>
</head>
<body>

<header>
  <div class="abs topbar">
    <svg class="abs home" width="16" height="14" viewBox="0 0 16 14"><path d="M8 1 1 7h2v6h4V9h2v4h4V7h2z" fill="#d9554f"/></svg>
    <div class="abs account"><a href="#">Your account</a><span>|</span><a href="#">Select Language ▾</a></div>
  </div>
  <nav class="abs mainnav">
    <div class="abs brand">LOGO</div>
    <div class="abs menu">
      <a class="active" href="#">How it works</a>
      <a href="#">Charity membership</a>
      <a href="#">Company fundraising</a>
      <a href="#">Pertnership</a>
      <a href="#">Contacts</a>
      <a href="#">Help</a>
    </div>
  </nav>
</header>

<section class="abs hero" role="img" aria-label="Sepia-toned photo of a school class standing in earthquake rubble, with a smiling child in the foreground"></section>
<div class="abs hero-caption">
  <p><b>DONATE</b> not only save their life,<br>also give them <b>JUSTICE...</b></p>
  <a class="more" href="#">Know more &gt;&gt;</a>
</div>
<div class="abs slider-dots"><i class="on"></i><i></i><i></i><i></i></div>

<section class="abs teaser">
  <div class="teaser-head">
    <h3>Teaser Panel <svg width="20" height="18" viewBox="0 0 20 18"><rect x="1" y="4" width="13" height="13" fill="none" stroke="#fff" stroke-width="1.6"/><path d="M4 9l4 4 10-12" fill="none" stroke="#fff" stroke-width="2.4"/></svg></h3>
    <h3>Teaser Panel <svg width="20" height="18" viewBox="0 0 20 18"><rect x="1" y="4" width="13" height="13" fill="none" stroke="#fff" stroke-width="1.6"/><path d="M4 9l4 4 10-12" fill="none" stroke="#fff" stroke-width="2.4"/></svg></h3>
  </div>
  <p class="teaser-col left">Lorem ipsum dolor sit amet, consectetur adipisicing elit, sed do eiusmod tempor incididunt ut labore et dolore magna aliqua. Ut enim ad minim veniam, quis nostrud exercitation ullamco laboris nisi ut aliquip ex ea commodo consequat. Duis aute irure dolor in reprehenderit in voluptate velit esse cillum dolore eu fugiat nulla pariatur. Excepteur sint occaecat cupidatat non proident, sunt in culpa qui officia deserunt mollit anim id est</p>
  <div class="abs teaser-divider"></div>
  <p class="teaser-col right">Lorem ipsum dolor sit amet, consectetur adipisicing elit, sed do eiusmod tempor incididunt ut labore et dolore magna aliqua. Ut enim ad minim veniam, quis nostrud exercitation ullamco laboris nisi ut aliquip ex ea commodo consequat. Duis aute irure dolor in reprehenderit in voluptate velit esse cillum dolore eu fugiat nulla pariatur. Excepteur sint occaecat cupidatat non proident, sunt in culpa qui officia deserunt mollit anim id est</p>
</section>

<nav class="abs sidenav">
  <a class="item" href="#"><svg width="12" height="10"><circle cx="4" cy="3" r="2.2" fill="#fff"/><circle cx="9" cy="3" r="2" fill="#fff"/><rect x="0" y="6" width="8" height="4" rx="2" fill="#fff"/><rect x="7" y="6" width="5" height="4" rx="2" fill="#fff"/></svg>How it works</a>
  <a class="item" href="#"><svg width="11" height="11"><rect x=".5" y=".5" width="10" height="10" fill="none" stroke="#fff"/><rect x="3" y="2" width="5" height="3" fill="#fff"/><rect x="3" y="6" width="5" height="3" fill="#fff"/></svg>Charity membership</a>
  <a class="item current" href="#"><svg width="12" height="10"><rect x=".5" y=".5" width="11" height="9" fill="none" stroke="#fff"/><path d="M2 8l3-3 2 2 2-2 2 3z" fill="#fff"/></svg>Company fundraising</a>
  <a class="sub" href="#">Submenu 1</a>
  <a class="sub" href="#">Submenu 2</a>
  <a class="sub" href="#">Submenu 3</a>
  <a class="item" href="#"><svg width="10" height="12"><circle cx="5" cy="4" r="3.5" fill="#fff"/><rect x="4" y="7" width="2" height="3" fill="#fff"/><rect x="2" y="10" width="6" height="2" fill="#fff"/></svg>Pertnership</a>
  <a class="item" href="#"><svg width="10" height="12"><circle cx="5" cy="3" r="2.5" fill="#fff"/><rect x="1" y="6" width="8" height="6" rx="1" fill="#fff"/></svg>Contact Us</a>
  <a class="item" href="#"><svg width="10" height="12"><circle cx="5" cy="3" r="2.5" fill="#fff"/><rect x="1" y="6" width="8" height="6" rx="1" fill="#fff"/></svg>Help</a>
</nav>

<main>
  <h2 class="abs section-title" style="left:300px;top:726px">Blogs goes &nbsp;here</h2>
  <div class="abs thumb" style="left:302px;top:757px;width:109px;height:70px;background:linear-gradient(135deg,#d9d4cf,#8d8a86 60%,#e6e2dc)" role="img" aria-label="Photo of hands stacked together in a circle"></div>
  <p class="abs blog-text" style="left:423px;top:753px;width:152px">Lorem ipsum dolor sit amet, consectetur adipisicing elit, sed do eiusmod tempor incididunt ut labore.</p>
  <div class="abs thumb" style="left:599px;top:757px;width:109px;height:70px;background:linear-gradient(135deg,#fff,#f2b9a3 50%,#fbe7df)" role="img" aria-label="Illustration of children playing together"></div>
  <p class="abs blog-text small" style="left:720px;top:753px;width:148px">Lorem ipsum dolor sit amet, consectetur adipisicing elit, sed do eiusmod tempor incididunt ut labore.</p>

  <h2 class="abs section-title" style="left:300px;top:843px">Popular on Friendbook</h2>
  <h2 class="abs section-title" style="left:598px;top:843px">Popular on Chirpline</h2>

  <div class="abs thumb" style="left:304px;top:873px;width:46px;height:56px;background:linear-gradient(#f4f4f4,#9a9a9a)" role="img" aria-label="Portrait photo of the post author"></div>
  <p class="abs post-text" style="left:363px;top:870px">Lorem ipsum dolor sit amet, consectetur adipisicing elit, sed do eiusmod tempor. <span class="date">Jan 12, 2013, Mara T. L.</span></p>
  <div class="abs thumb" style="left:304px;top:940px;width:46px;height:56px;background:linear-gradient(#f4f4f4,#9a9a9a)" role="img" aria-label="Portrait photo of the post author"></div>
  <p class="abs post-text" style="left:363px;top:936px">Lorem ipsum dolor sit amet, consectetur adipisicing elit, sed do eiusmod tempor. <span class="date">Jan 12, 2013, Mara T. L.</span></p>

  <div class="abs thumb" style="left:601px;top:873px;width:46px;height:56px;background:linear-gradient(#f4f4f4,#9a9a9a)" role="img" aria-label="Portrait photo of the post author"></div>
  <p class="abs post-text" style="left:660px;top:870px">Lorem ipsum dolor sit amet, consectetur adipisicing elit, sed do eiusmod tempor. <span class="date">Jan 12, 2013, Mara T. L.</span></p>
  <div class="abs thumb" style="left:601px;top:940px;width:46px;height:56px;background:linear-gradient(#f4f4f4,#9a9a9a)" role="img" aria-label="Portrait photo of the post author"></div>
  <p class="abs post-text" style="left:660px;top:936px">Lorem ipsum dolor sit amet, consectetur adipisicing elit, sed do eiusmod tempor. <span class="date">Jan 12, 2013, Mara T. L.</span></p>
</main>

<footer class="abs footer">
  <div class="fcol" style="left:81px;width:90px"><h4>How it works</h4><a href="#">Headline 1</a><a href="#">Headline 1</a><a href="#">Headline 1</a></div>
  <div class="fcol" style="left:185px;width:125px"><h4>Charity membership</h4><a href="#">Headline 1</a><a href="#">Headline 1</a><a href="#">Headline 1</a></div>
  <div class="fcol" style="left:338px;width:125px"><h4>Company fundraising</h4><a href="#">Headline 1</a><a href="#">Headline 1</a><a href="#">Headline 1</a></div>
  <div class="fcol" style="left:501px;width:103px"><h4>Pertnership</h4><a href="#">Headline 1</a><a href="#">Headline 1</a><a href="#">Headline 1</a></div>
  <div class="abs subscribe" style="width:200px;height:120px">
    Subscribe us :
    <div class="email">Your email address<span class="go"><svg width="16" height="12" viewBox="0 0 16 12"><path d="M1 6l5 5L15 1" fill="none" stroke="#fff" stroke-width="2.4"/></svg></span></div>
    <div class="follow">Follow us :</div>
    <div class="socials" aria-label="Social links"><span></span><span></span><span></span><span></span><span></span></div>
  </div>
</footer>
<div class="abs copyright">Copyright @ 2013, Company name, All rights are reserved.</div>

</body>
</html>
```